sydney wedding photography business needs a business card design

we need a business card design for a sydney based wedding photography and videography business. our business name is :golden hour studios and film. our target clients are 24-35 yrs female. our style is candid, organic, natural, dynamic. we are a team of young photographers and videographers, and help brides to create memories that they will cherish for the rest of their lives. the logo will be provided. we want an elegant design that reflects our style, and also want to give a great impression to our clients that we are one of the best studios in sydney and our brand means quality and premium service.

Target Market(s)

bride to be, 24-35 years old, living in sydney and surrunding areas

Industry/Entity Type

Wedding Photography

Contact Information for Business Card

address: 47 marrowbank street, fernhill nsw 2077
mobile: 0417283951
phone: (02) 9163 2748
info@goldenhourstudio.net.au
www.goldenhourstudio.net.au
facebook:goldenhourbridals
instagram:goldenhourbridals

Font styles to use
Serif
Sans Serif

Requirements
Nice to have
• maybe add my slogan"moments that last forever" if the layout looks good
Should not have
• no black color, not good idea for wedding biz card

```html
<!DOCTYPE html>
<html lang="en">
<head>
<meta charset="utf-8">
<title>Golden Hour Studios and Film – Business Card</title>
<link href="https://fonts.googleapis.com/css2?family=Arvo:wght@700&family=Lora:wght@400;500&display=swap" rel="stylesheet">
<style>
  :root {
    --page: #eeeeee;
    --gold: #f2b705;
    --ink: #3a3530;
    --veil: rgba(255, 252, 244, 0.82);
    --photo-warm-a: #f1e6d8;
    --photo-warm-b: #c9b8d6;
    --photo-warm-c: #e9dccd;
    --photo-cool-a: #1f3a2c;
    --photo-cool-b: #f3efe8;
  }
  html, body {
    margin: 0;
    padding: 0;
    width: 1200px;
    height: 777px;
    overflow: hidden;
    background: var(--page);
  }
  .canvas {
    position: relative;
    width: 1200px;
    height: 777px;
  }
  .card {
    position: absolute;
    top: 229px;
    width: 520px;
    height: 318px;
    overflow: hidden;
    box-shadow: 0 6px 18px rgba(0, 0, 0, 0.12);
  }
  .card--contact { left: 50px; }
  .card--front { left: 630px; }

  .photo {
    position: absolute;
    inset: 0;
  }
  .card--contact .photo {
    background:
      radial-gradient(ellipse 45% 60% at 28% 62%, var(--photo-warm-b), transparent 70%),
      linear-gradient(120deg, var(--photo-warm-c), var(--photo-warm-a) 55%, #faf5ec);
  }
  .card--front .photo {
    background:
      radial-gradient(ellipse 30% 55% at 62% 58%, #e7a6a0 0%, transparent 60%),
      linear-gradient(90deg, var(--photo-cool-a) 0%, #3c5742 22%, var(--photo-cool-b) 40%, var(--photo-cool-b) 68%, #4a5e45 84%, var(--photo-cool-a) 100%);
  }
  .veil {
    position: absolute;
    top: 0; right: 0; bottom: 0;
    width: 58%;
    background: linear-gradient(90deg, rgba(255,252,244,0) 0%, var(--veil) 30%);
  }
  .frame {
    position: absolute;
    inset: 0;
  }

  .brand-name {
    font-family: "Arvo", serif;
    font-weight: 700;
    color: var(--gold);
    margin: 0;
    white-space: nowrap;
  }
  .card--contact .brand-name {
    position: absolute;
    left: 258px;
    top: 34px;
    font-size: 17px;
    line-height: 1.15;
  }
  .contact-list {
    position: absolute;
    left: 258px;
    top: 92px;
    margin: 0;
    padding: 0;
    list-style: none;
    font-family: "Lora", serif;
    color: var(--ink);
  }
  .contact-list li {
    display: flex;
    align-items: center;
    gap: 7px;
    font-size: 10.5px;
    line-height: 1.8;
    white-space: nowrap;
  }
  .contact-list li.contact-list__main { font-size: 16px; line-height: 1.45; }
  .contact-list svg { width: 11px; height: 11px; flex: none; }
  .social-row {
    position: absolute;
    left: 258px;
    bottom: 22px;
    display: flex;
    gap: 14px;
    font-family: "Lora", serif;
    font-size: 10px;
    color: var(--ink);
  }
  .social-row span { display: flex; align-items: center; gap: 5px; }
  .social-dot {
    width: 8px; height: 8px; border-radius: 50%;
    background: var(--gold);
  }

  .slogan {
    position: absolute;
    left: 0; right: 0;
    top: 128px;
    margin: 0;
    text-align: center;
    font-family: "Arvo", serif;
    font-weight: 700;
    font-size: 26px;
    color: var(--gold);
  }
  .card--front .brand-name {
    position: absolute;
    left: 0; right: 0;
    bottom: 58px;
    text-align: center;
    font-size: 22px;
  }
</style>
</head>
<body>
<main class="canvas">

  <section class="card card--contact" aria-label="Business card, contact side">
    <div class="photo" role="img" aria-label="Photograph of a bride and groom holding a purple and white rose bouquet"></div>
    <div class="veil"></div>
    <svg class="frame" viewBox="0 0 520 318" aria-hidden="true">
      <polyline points="242,20 505,20 505,215" fill="none" stroke="var(--gold)" stroke-width="3"/>
      <line x1="505" y1="232" x2="505" y2="246" stroke="var(--gold)" stroke-width="3"/>
    </svg>
    <p class="brand-name">Golden Hour Studios<br>and Film</p>
    <ul class="contact-list">
      <li class="contact-list__main">
        <svg viewBox="0 0 12 12"><path d="M3 1h2l1 3-1.5 1a6 6 0 0 0 2.5 2.5L8 6l3 1v2a2 2 0 0 1-2 2A8 8 0 0 1 1 3a2 2 0 0 1 2-2z" fill="var(--gold)"/></svg>
        0417283951
      </li>
      <li class="contact-list__main">
        <svg viewBox="0 0 12 12"><rect x="1" y="5" width="10" height="6" rx="1" fill="var(--gold)"/><path d="M1 5a5 3 0 0 1 10 0" fill="none" stroke="var(--gold)" stroke-width="1.6"/></svg>
        (02) 9163 2748
      </li>
      <li>
        <svg viewBox="0 0 12 12"><rect x="1" y="2.5" width="10" height="7" fill="var(--gold)"/><polyline points="1,3 6,7 11,3" fill="none" stroke="#fff" stroke-width="1"/></svg>
        info@goldenhourstudio.net.au
      </li>
      <li>
        <svg viewBox="0 0 12 12"><circle cx="6" cy="6" r="5" fill="var(--gold)"/><path d="M1 6h10M6 1a7 5 0 0 1 0 10M6 1a7 5 0 0 0 0 10" fill="none" stroke="#fff" stroke-width=".8"/></svg>
        www.goldenhourstudio.net.au
      </li>
      <li>
        <svg viewBox="0 0 12 12"><path d="M6 11S2 6.8 2 4.5a4 4 0 0 1 8 0C10 6.8 6 11 6 11z" fill="var(--gold)"/><circle cx="6" cy="4.5" r="1.4" fill="#fff"/></svg>
        47 marrowbank street, fernhill nsw 2077
      </li>
    </ul>
    <div class="social-row">
      <span><i class="social-dot"></i>goldenhourbridals</span>
      <span><i class="social-dot"></i>goldenhourbridals</span>
    </div>
  </section>

  <section class="card card--front" aria-label="Business card, front side">
    <div class="photo" role="img" aria-label="Photograph of a bride in a white gown and veil holding a pastel flower bouquet"></div>
    <svg class="frame" viewBox="0 0 520 318" aria-hidden="true">
      <polyline points="120,58 30,58 30,292 240,292" fill="none" stroke="var(--gold)" stroke-width="3"/>
      <polyline points="400,30 488,30 500,268 430,270" fill="none" stroke="var(--gold)" stroke-width="3"/>
    </svg>
    <p class="slogan">Moments that last forever</p>
    <p class="brand-name">Golden Hour Studios and Film</p>
  </section>

</main>
</body>
</html>
```